Brisk Meadow Builders needs a product brochure

We need a new flyer for our Patio Perch Lounge. Here is some of the copy your will need.
"Turn your back yard into the ultimate entertianment venue with the stunning Patio Perch Lounge!"
"Entertain family & friends in your very own back yard!"
"Available with or without solar and comes in a variety of colors"
"The Patio Perch Lounge measures 5' deep by 10' wide and is 9'-6" at it's highest point"
"Constructed with treated 4x4's, primed then painted with Thornby Calder best exterior paint for years of care free enjoyment. Also, Marlow Pendt Keystead shingles are dimensional, have a 25 year warranty and are rated for 150 mph winds!"
"TV Mount included. Shelves and TV are sold separately"
There also needs to be a box where we can add the price into later. The price can change from time to time due to material cost fluctuation.
Look and feel
Each slider illustrates characteristics of the customer's brand and the style your logo design should communicate.

```html
<!DOCTYPE html>
<html lang="en">
<head>
<meta charset="utf-8">
<title>Patio Perch Lounge Flyer</title>
<link rel="stylesheet" href="https://fonts.googleapis.com/css2?family=Barlow:wght@400;500;700;800&family=Barlow+Semi+Condensed:wght@600;700;800&display=swap">
<style>
:root{
  --mat:#262626;
  --paper:#ffffff;
  --green:#2e7a3c;
  --green-dark:#256b31;
  --green-light:#3d8f49;
  --orange:#f5a81c;
  --ink:#1b1b1b;
}
*{margin:0;padding:0;box-sizing:border-box}
html,body{width:810px;height:1200px;overflow:hidden;background:var(--mat)}
.flyer{position:absolute;left:45px;top:90px;width:720px;height:1022px;background:var(--paper);overflow:hidden;font-family:"Barlow",sans-serif}
.backdrop{position:absolute;left:0;top:0;width:720px;height:1022px}
.brand{position:absolute;left:30px;top:64px;display:flex;align-items:center;gap:8px;font-family:"Barlow",sans-serif;font-weight:700;font-size:19px;line-height:21px;color:var(--green);letter-spacing:.5px}
.brand .dot{flex:none;width:14px;height:14px;border-radius:50%;background:var(--orange)}
.headline{position:absolute;left:44px;top:458px;font-family:"Barlow Semi Condensed",sans-serif;font-weight:700;font-size:33px;line-height:32px;color:#fff}
.headline .accent{color:var(--orange)}
.venue{position:absolute;left:382px;top:460px;width:340px;text-align:center;font-family:"Barlow Semi Condensed",sans-serif;color:#fff}
.venue .lead{font-weight:700;font-size:20px;line-height:23px}
.venue .product{font-family:"Barlow",sans-serif;font-weight:800;font-size:35px;line-height:37px;color:var(--orange);letter-spacing:1px;margin-top:6px}
.thumb{position:absolute;top:550px;width:175px;height:142px;border:4px solid var(--green);border-radius:16px}
.thumb.opener{left:18px;background:linear-gradient(135deg,#b9bdb5,#6f6a60 55%,#9c5a3a)}
.thumb.rack{left:205px;background:linear-gradient(180deg,#3a3a3e 0 45%,#c07a44 45%,#a2602f)}
.features{position:absolute;left:16px;top:700px;width:385px;height:263px;border-radius:20px;background:linear-gradient(135deg,var(--green-dark),var(--green-light) 55%,var(--green-dark));color:#fff;padding:12px 14px 0 30px;list-style:none;font-size:13.3px;line-height:20.5px}
.features li{position:relative;margin-bottom:10px}
.features li::before{content:"";position:absolute;left:-20px;top:6px;width:8px;height:8px;border-radius:50%;background:#fff}
.features li.justify{text-align:justify}
.invite{position:absolute;left:440px;top:686px;width:242px;text-align:center;font-size:20.5px;line-height:27px;color:var(--ink)}
.invite strong{display:block;font-weight:700;color:var(--green)}
.price-box{position:absolute;left:463px;top:786px;width:197px;height:160px;border-radius:16px;background:linear-gradient(135deg,var(--green-dark),var(--green-light) 55%,var(--green-dark));color:#fff;text-align:center;padding-top:14px;font-size:25.5px;line-height:29px;font-weight:500}
.contact{position:absolute;left:0;top:979px;width:720px;height:43px;background:var(--orange);display:flex;align-items:center;font-size:15.3px;color:var(--ink)}
.contact span{position:absolute;display:flex;align-items:center;gap:9px}
.contact svg{width:15px;height:15px}
</style>
</head>
<body>
<div class="flyer">
  <svg class="backdrop" viewBox="0 0 720 1022">
    <defs>
      <linearGradient id="photo" x1="0" y1="0" x2="0" y2="1">
        <stop offset="0" stop-color="#8da65a"/>
        <stop offset=".3" stop-color="#4a4c50"/>
        <stop offset=".55" stop-color="#b57a3f"/>
        <stop offset=".8" stop-color="#3d3f44"/>
        <stop offset="1" stop-color="#9fa2a4"/>
      </linearGradient>
      <linearGradient id="band" x1="0" y1="0" x2="1" y2="1">
        <stop offset="0" stop-color="#256b31"/>
        <stop offset=".5" stop-color="#3d8f49"/>
        <stop offset="1" stop-color="#256b31"/>
      </linearGradient>
    </defs>
    <polygon points="0,213 462,0 520,0 120,193 120,345 0,302" fill="var(--orange)"/>
    <path d="M0,302 L76,342 C200,400 320,440 420,470 L0,470 Z" fill="var(--orange)"/>
    <polygon role="img" aria-label="Photo of the Patio Perch Lounge backyard bar with solar panel roof, TV, shelves and bar stools on a patio" points="76,193 460,0 720,0 720,383 390,470 76,342" fill="url(#photo)"/>
    <path d="M0,383 C150,440 300,462 410,470 L410,535 L0,535 Z" fill="url(#band)"/>
    <path d="M720,375 C700,410 680,425 650,440 L720,440 Z" fill="var(--orange)"/>
    <ellipse cx="556" cy="542" rx="178" ry="131" fill="#fff"/>
    <ellipse cx="556" cy="542" rx="172" ry="125" fill="url(#band)"/>
    <path d="M401,870 C430,872 450,868 458,867 L458,920 C440,922 420,922 401,922 Z" fill="var(--orange)"/>
    <path d="M720,770 C700,810 680,830 665,840 L665,830 C690,810 705,790 720,760 Z" fill="var(--orange)"/>
  </svg>

  <div class="brand"><span class="dot"></span><span>BRISK MEADOW<br>BUILDERS</span></div>

  <h1 class="headline">TURN<br>YOUR&nbsp; <span class="accent">BACK YARD INTO</span></h1>

  <div class="venue">
    <p class="lead">THE ULTIMATE<br>ENTERTIANMENT VENUE<br>WITH</p>
    <p class="product">THE STUNNING<br>PATIO PERCH<br>LOUNGE!</p>
  </div>

  <div class="thumb opener" role="img" aria-label="Photo of a hand opening a bottle on a post-mounted bottle opener beside a football"></div>
  <div class="thumb rack" role="img" aria-label="Photo of a wine shelf with bottles above hanging copper wine glasses"></div>

  <ul class="features">
    <li>Available with or without solar and comes<br>in a variety of colors</li>
    <li>The Patio Perch Lounge measures 5' deep by<br>10' wide and is 9'-6" at it's highest point</li>
    <li>TV Mount included. Shelves and TV are sold separately</li>
    <li class="justify">Constructed with treated 4x4's, primed then painted with Thornby Calder best exterior paint for years of care free enjoyment. Also, Marlow Pendt Keystead shingles are dimensional, have a 25 year warranty and are rated for 150 mph winds!</li>
  </ul>

  <p class="invite">Entertain family &amp; friends<br>in your<strong>very own back yard!</strong></p>

  <div class="price-box">STARTING<br>AT JUST</div>

  <div class="contact">
    <span style="left:48px"><svg viewBox="0 0 16 16"><circle cx="8" cy="8" r="8" fill="#fff"/><rect x="4" y="5" width="8" height="6" fill="none" stroke="var(--orange)" stroke-width="1.3"/><path d="M4 5 L8 8.5 L12 5" fill="none" stroke="var(--orange)" stroke-width="1.3"/></svg>hello@briskmeadowbuilders.com</span>
    <span style="left:302px"><svg viewBox="0 0 16 16"><circle cx="8" cy="8" r="8" fill="#fff"/><circle cx="8" cy="8" r="4.5" fill="none" stroke="var(--orange)" stroke-width="1.3"/><path d="M3.5 8 H12.5 M8 3.5 V12.5" stroke="var(--orange)" stroke-width="1.1"/></svg>www.briskmeadowbuilders.com</span>
    <span style="left:555px"><svg viewBox="0 0 16 16"><circle cx="8" cy="8" r="8" fill="#fff"/><path d="M5 4 L7 4 L7.6 6.3 L6.5 7.2 C7 8.4 7.8 9.2 9 9.7 L9.9 8.6 L12 9.2 L12 11.2 C8 11.5 4.6 8 5 4 Z" fill="var(--orange)"/></svg>555-310-0188</span>
  </div>
</div>
</body>
</html>
```